website refresh/redesign needed for Printing e commerce website

We'd like a website refresh/redesign done with the specific goal of having the site act as a more effective funnel for leads.<br/><br/>We think that the current design is outdated.<br/><br/>We want our customers and partners to still recognize the website, Is a big chunk of our business is repeat orders. <br/>so it should not be a full redesign. General color scheme and such should remain the same so that it is clear we are the same company. <br/><br/>However, the updated website design should look more polished and convey high-quality products and services that we provide. <br/><br/>Our website is https://shopledgerformsnet.quillpaperdepot.com/ if you want to take a look at our current website design. <br/><br/>we need 3 pages redesigned... <br/><br/>1. homepage:https://shopledgerformsnet.quillpaperdepot.com/<br/><br/>2. Category page: <br/>https://shopledgerformsnet.quillpaperdepot.com/order-computer-checks-c-4.html<br/><br/>3. Product detail page: https://shopledgerformsnet.quillpaperdepot.com/voucher-computer-checks-p-35.html<br/><br/> I can provide many more pictures of our products if needed.<br/><br/><br/>BTW. I have another project here on brief bazaar, you can check the other ones too, so to make it easier to do both when working on this.<br/><br/> Please reach out to me should you have any questions or comments.

```html
<!DOCTYPE html>
<html lang="en">
<head>
<meta charset="utf-8">
<title>Computer Checks – ShopLedgerForms</title>
<link href="https://fonts.googleapis.com/css2?family=Arimo:wght@400;700&display=swap" rel="stylesheet">
<style>
:root{
  --header-bg:#2b2b2b;
  --brand-green:#7fe05a;
  --accent-green:#9ee27f;
  --soft-green:#c8e8bd;
  --btn-green:#2a4e16;
  --page-bg:#f7f7f7;
  --panel:#ffffff;
  --text:#222222;
  --muted:#555555;
  --line:#555555;
  --light-line:#dddddd;
  --footer-bg:#e4e9e4;
  --check-blue:#b8c6ea;
  --check-edge:#3e5fc4;
}
*{box-sizing:border-box;margin:0;padding:0}
html,body{width:1200px;height:2977px;overflow:hidden}
body{font-family:"Arimo",Arial,sans-serif;color:var(--text);background:var(--page-bg);position:relative}
.abs{position:absolute}
a{color:inherit;text-decoration:none}

.site-header{left:0;top:0;width:1200px;height:83px;background:var(--header-bg)}
.brand{left:87px;top:27px;display:flex;align-items:center;gap:8px;color:var(--brand-green);font-weight:700;font-size:22px}
.brand-dot{width:12px;height:12px;border-radius:50%;background:var(--brand-green)}
.header-links{right:62px;top:34px;display:flex;gap:28px;color:#fff;font-size:11px;font-weight:700}
.cart-count{display:inline-block;width:19px;height:19px;border-radius:50%;background:#fff;color:#222;text-align:center;line-height:19px;margin-left:4px;font-size:10px}
.main-nav{left:0;top:83px;width:1200px;height:50px;background:#fff;border-bottom:1px solid #eee}
.nav-item{top:19px;font-size:12px;color:#222}
.nav-sep{top:18px;width:1px;height:14px;background:#ddd}
.nav-right{top:19px;font-size:10.5px;font-weight:700}

.breadcrumb{left:62px;top:167px;font-size:11px;letter-spacing:.3px}
.finder{top:157px;height:22px;border-bottom:1px solid #333;font-size:10.5px;padding:3px 7px;width:159px}
.finder::after{content:"";position:absolute;right:6px;top:8px;border:4px solid transparent;border-top-color:#333}
.page-title{left:62px;top:246px;font-size:26px;font-weight:700;letter-spacing:3px}

.config-panel{left:62px;top:326px;width:434px;height:1917px;background:var(--panel);box-shadow:0 0 3px rgba(0,0,0,.12)}
.step-tabs{left:0;top:0;width:434px;height:69px}
.step{top:0;height:69px;display:flex;align-items:center;justify-content:center;text-align:center;font-size:8.5px;letter-spacing:1px;line-height:1.6}
.step.active{background:#e9ece8;border-bottom:5px solid var(--accent-green);font-weight:700}
.step-sep{top:30px;width:1px;height:12px;background:#ddd}
.section-title{left:17px;font-size:14px;font-weight:700;letter-spacing:1.5px;display:flex;align-items:center;gap:6px}
.info-dot{width:11px;height:11px;border-radius:50%;background:#222;color:#fff;font-size:8px;text-align:center;line-height:11px}
.type-option{width:61px;height:85px;border:1px solid #bbb;background:#fff}
.type-option.selected{border:4px solid var(--accent-green)}
.type-band{position:absolute;left:4px;right:4px;background:var(--soft-green)}
.field{left:17px;width:400px;height:24px;border-bottom:1px solid var(--line);font-size:12.5px;font-style:italic;letter-spacing:1px;color:#444;padding-left:10px}
.field.select::after{content:"";position:absolute;right:6px;top:7px;border:4px solid transparent;border-top-color:#333}
.software-list{left:17px;top:383px;width:400px;height:219px;background:#fff;box-shadow:0 1px 4px rgba(0,0,0,.18);padding:22px 0 0 17px}
.software-list li{list-style:none;font-size:12px;letter-spacing:.9px;height:25px;white-space:nowrap}
.scrollbar{right:10px;top:22px;width:6px;height:38px;border-radius:3px;background:#ccc}
.option{left:17px;font-size:12px;letter-spacing:.9px;display:flex;align-items:center;gap:4px}
.box{width:9px;height:9px;border:1px solid #333}
.radio{width:10px;height:10px;border:1px solid #333;border-radius:50%;position:relative}
.radio.on::after{content:"";position:absolute;left:2px;top:2px;width:4px;height:4px;border-radius:50%;background:#333}
.qty-select{left:17px;top:993px;width:400px;height:24px;border-bottom:1px solid var(--line);font-size:10.5px;padding:2px 10px}
.qty-select::after{content:"";position:absolute;right:6px;top:7px;border:4px solid transparent;border-top-color:#333}
.swatch-highlight{left:22px;top:1117px;width:78px;height:164px;background:#c4c4c4}
.swatch{width:56px}
.swatch-thumb{width:56px;height:72px;border:1px solid #aaa}
.swatch-label{margin-top:11px;font-size:10.5px;color:#777;text-align:center;line-height:11.5px;width:60px;margin-left:-2px}
.swatch.current .swatch-label{color:#222}
.next-btn{left:96px;top:1822px;width:242px;height:44px;background:var(--btn-green);color:#fff;font-weight:700;font-size:14px;letter-spacing:1.5px;display:flex;align-items:center;justify-content:center}

.preview-panel{left:521px;top:326px;width:616px;height:899px;background:var(--panel);box-shadow:0 0 3px rgba(0,0,0,.12)}
.check-face{left:8px;top:53px;width:602px;height:215px;border:2px solid var(--check-edge);border-top-width:6px;border-radius:4px;background:linear-gradient(160deg,#c6d1ee 0%,#aebde6 35%,#c9d3ef 60%,#b1c0e7 100%)}
.check-notice{left:0;top:-7px;width:100%;text-align:center;font-size:5px;color:#fff;font-weight:700;letter-spacing:.2px}
.check-side{right:6px;top:60px;writing-mode:vertical-rl;transform:rotate(180deg);font-size:5px;color:#5b74c9}
.perforation{left:6px;width:604px;border-top:1px dashed #aaa}
.stub{left:10px;width:598px;height:244px;border-radius:4px;background:linear-gradient(180deg,#c6cff0,#d1d8f2)}
.preview-fade{left:6px;top:840px;width:604px;height:25px;background:#f4f5fa}

.desc-tabs{left:234px;top:2309px;width:734px;height:46px}
.desc-tab{top:0;height:46px;display:flex;align-items:center;justify-content:center;font-size:11px;letter-spacing:1.2px}
.desc-tab.active{background:#fff;font-weight:700}
.desc-body{left:234px;top:2355px;width:734px;height:198px;background:#fff;padding:28px 24px;font-size:12.5px;letter-spacing:.9px}

.site-footer{left:0;top:2680px;width:1200px;height:245px;background:var(--footer-bg)}
.foot-head{font-size:8.5px;font-weight:700;letter-spacing:1.3px}
.foot-links li{list-style:none;font-size:11px;letter-spacing:.9px;height:25px}
.social{width:17px;height:17px;border-radius:3px}
.newsletter-badge{left:62px;top:182px;width:104px;height:18px;background:#2f8f1f;color:#fff;font-size:8px;font-weight:700;line-height:18px;padding-left:22px;border-radius:2px}
.newsletter-badge::before{content:"";position:absolute;left:3px;top:2px;width:14px;height:14px;background:#f1c24a;border-radius:2px}
.bottom-bar{left:0;top:2925px;width:1200px;height:52px;background:#fff}
.safe-badge{left:62px;top:17px;width:72px;height:18px;background:#3b8f1e;border-radius:2px}
.copyright{left:0;top:21px;width:1200px;text-align:center;font-size:9px;letter-spacing:.6px}
.pay-mark{top:17px;height:16px;border-radius:2px}
</style>
</head>
<body>

<header class="abs site-header">
  <a class="abs brand" href="https://shopledgerformsnet.quillpaperdepot.com/"><span class="brand-dot"></span>ShopLedgerForms</a>
  <div class="abs header-links"><span>&#128722; Cart <span class="cart-count">0</span></span><span>&#9679; Log in | Register</span></div>
</header>

<nav class="abs main-nav">
  <span class="abs nav-item" style="left:62px">Business Checks ▾</span>
  <span class="abs nav-sep" style="left:178px"></span>
  <span class="abs nav-item" style="left:194px">Computer Checks ▾</span>
  <span class="abs nav-sep" style="left:313px"></span>
  <span class="abs nav-item" style="left:331px">Tallyworks Checks ▾</span>
  <span class="abs nav-sep" style="left:460px"></span>
  <span class="abs nav-item" style="left:477px">Accessories ▾</span>
  <span class="abs nav-sep" style="left:565px"></span>
  <span class="abs nav-item" style="left:584px">Reorder</span>
  <span class="abs nav-right" style="left:971px">&#9679; Help/FAQs ▾</span>
  <span class="abs nav-right" style="left:1074px">&#9742; Contact Us</span>
</nav>

<div class="abs breadcrumb">Home › Computer Checks › Order Computer Checks</div>
<div class="abs finder" style="left:613px">Order Status</div>
<div class="abs finder" style="left:795px">Search by Software Checks</div>
<div class="abs finder" style="left:978px">Quick Finder</div>

<h1 class="abs page-title">COMPUTER CHECKS</h1>

<section class="abs config-panel">
  <div class="abs step-tabs">
    <div class="abs step active" style="left:0;width:109px">QUANTITY &amp;<br>COLOR</div>
    <div class="abs step" style="left:109px;width:108px">CUSTOMER INFO</div>
    <span class="abs step-sep" style="left:217px"></span>
    <div class="abs step" style="left:217px;width:109px">BANK INFO</div>
    <span class="abs step-sep" style="left:326px"></span>
    <div class="abs step" style="left:326px;width:108px">ADDITIONAL<br>OPTION<br>&amp; CHECKOUTS</div>
  </div>

  <h2 class="abs section-title" style="top:115px">SELECT CHECK TYPE <span class="info-dot">i</span></h2>
  <div class="abs type-option selected" style="left:17px;top:155px;width:80px;height:103px">
    <span class="type-band" style="top:8px;height:24px"></span>
  </div>
  <div class="abs type-option" style="left:106px;top:164px"><span class="type-band" style="top:32px;height:21px"></span></div>
  <div class="abs type-option" style="left:188px;top:164px"><span class="type-band" style="bottom:4px;height:21px"></span></div>
  <div class="abs type-option" style="left:266px;top:164px">
    <span class="type-band" style="top:4px;height:23px"></span><span class="type-band" style="top:30px;height:23px"></span><span class="type-band" style="top:56px;height:23px"></span>
  </div>
  <div class="abs type-option" style="left:345px;top:164px">
    <span class="type-band" style="left:22px;top:4px;height:23px"></span><span class="type-band" style="left:22px;top:30px;height:23px"></span><span class="type-band" style="left:22px;top:56px;height:23px"></span>
    <svg class="abs" style="left:5px;top:8px" width="14" height="68" viewBox="0 0 14 68"><g stroke="#999" stroke-width="1"><line x1="0" y1="2" x2="12" y2="2"/><line x1="0" y1="8" x2="8" y2="8"/><line x1="0" y1="28" x2="12" y2="28"/><line x1="0" y1="34" x2="8" y2="34"/><line x1="0" y1="54" x2="12" y2="54"/><line x1="0" y1="60" x2="8" y2="60"/></g></svg>
  </div>

  <h2 class="abs section-title" style="top:307px">CHECK LAYOUT <span class="info-dot">i</span></h2>
  <div class="abs field select" style="top:348px">Search Software</div>
  <div class="abs software-list">
    <ul>
      <li>Formline Tax</li>
      <li>Brightpath Payroll Suite</li>
      <li>Cobalt Clinic Office (Harbor)</li>
      <li>Northgate Books</li>
      <li>Quarry Legal Desk</li>
      <li>Willow Fund Ledger (Tallybook) (FR-204)</li>
      <li>Willow Fund Ledger (Tallybook) (FR-204)</li>
    </ul>
    <span class="abs scrollbar"></span>
  </div>
  <div class="abs field" style="top:636px">Enter Software Version &amp; Year</div>

  <h2 class="abs section-title" style="top:708px">DIRECT DEPOSIT ADVICE <span class="info-dot">i</span></h2>
  <label class="abs option" style="top:752px"><span class="box"></span> Don't print the account and routing number</label>

  <h2 class="abs section-title" style="top:815px">SECURITY FEATURES <span class="info-dot">i</span></h2>
  <label class="abs option" style="top:860px"><span class="radio on"></span> Regular Security</label>
  <label class="abs option" style="top:893px"><span class="radio"></span> High Security</label>

  <h2 class="abs section-title" style="top:956px">QUANTITY</h2>
  <div class="abs qty-select">"ON SALE" 1000 Checks + 500 Self-Seal Check Envelopes ( $111.99 )</div>

  <h2 class="abs section-title" style="top:1068px">COLOR</h2>
  <div class="abs swatch-highlight"></div>

  <div class="abs swatch current" style="left:35px;top:1128px"><div class="swatch-thumb" role="img" aria-label="Marble blue check paper" style="background:linear-gradient(180deg,#6e8ee6 0 30%,#c3d0f4 30% 65%,#aabbee 65%)"></div><div class="swatch-label">Marble Blue (Default) (cot)</div></div>
  <div class="abs swatch" style="left:113px;top:1128px"><div class="swatch-thumb" role="img" aria-label="Marble green check paper" style="background:linear-gradient(180deg,#8fcf9f 0 30%,#d4eedb 30% 65%,#c0e4c9 65%)"></div><div class="swatch-label">Marble Green (cot)</div></div>
  <div class="abs swatch" style="left:190px;top:1128px"><div class="swatch-thumb" role="img" aria-label="Marble burgundy check paper" style="background:linear-gradient(180deg,#e4a6b0 0 30%,#f3dde1 30% 65%,#ecccd2 65%)"></div><div class="swatch-label">Marble Burgundy (cot)</div></div>
  <div class="abs swatch" style="left:268px;top:1128px"><div class="swatch-thumb" role="img" aria-label="Marble purple check paper" style="background:linear-gradient(180deg,#c3a5ea 0 30%,#ecdcf7 30% 65%,#e1cbf3 65%)"></div><div class="swatch-label">Marble Purple (cot)</div></div>
  <div class="abs swatch" style="left:345px;top:1128px"><div class="swatch-thumb" role="img" aria-label="Marble yellow gold check paper" style="background:linear-gradient(180deg,#f0df8a 0 30%,#faf2c7 30% 65%,#f6ebb1 65%)"></div><div class="swatch-label">Marble Yellow Gold (cot)</div></div>

  <div class="abs swatch" style="left:35px;top:1304px"><div class="swatch-thumb" role="img" aria-label="Classic blue check paper" style="background:linear-gradient(180deg,#4a6bc8 0 5%,#b5c8ee 5% 35%,#d3dff5 35% 67%,#c3d3f1 67%)"></div><div class="swatch-label">Classic Blue (cot)</div></div>
  <div class="abs swatch" style="left:113px;top:1304px"><div class="swatch-thumb" role="img" aria-label="Classic green check paper" style="background:linear-gradient(180deg,#4fae67 0 5%,#c7e7cf 5% 35%,#dcf0e0 35% 67%,#cfe9d5 67%)"></div><div class="swatch-label">Classic Green (cot)</div></div>
  <div class="abs swatch" style="left:190px;top:1304px"><div class="swatch-thumb" role="img" aria-label="Classic burgundy check paper" style="background:linear-gradient(180deg,#d67685 0 5%,#f0c8cf 5% 35%,#f5dde1 35% 67%,#f1d1d7 67%)"></div><div class="swatch-label">Classic Burgundy (cot)</div></div>
  <div class="abs swatch" style="left:268px;top:1304px"><div class="swatch-thumb" role="img" aria-label="Classic purple check paper" style="background:linear-gradient(180deg,#5e5f9e 0 5%,#a7a9d2 5% 35%,#c7c8e4 35% 67%,#b7b8db 67%)"></div><div class="swatch-label">Classic Purple (cot)</div></div>
  <div class="abs swatch" style="left:345px;top:1304px"><div class="swatch-thumb" role="img" aria-label="Classic yellow gold check paper" style="background:linear-gradient(180deg,#d6c27c 0 5%,#f1e6b9 5% 35%,#f7efcf 35% 67%,#f3e9c1 67%)"></div><div class="swatch-label">Classic Yellow Gold (cot)</div></div>

  <div class="abs swatch" style="left:35px;top:1481px"><div class="swatch-thumb" role="img" aria-label="Linen blue check paper" style="background:linear-gradient(180deg,#8fa2d8 0 30%,#b9c6ea 30% 65%,#a8b8e3 65%)"></div><div class="swatch-label">Linen Blue (cot)</div></div>
  <div class="abs swatch" style="left:113px;top:1481px"><div class="swatch-thumb" role="img" aria-label="Linen green check paper" style="background:linear-gradient(180deg,#9ac8a6 0 30%,#c5e1cc 30% 65%,#b3d7bd 65%)"></div><div class="swatch-label">Linen Green (cot)</div></div>
  <div class="abs swatch" style="left:190px;top:1481px"><div class="swatch-thumb" role="img" aria-label="Linen burgundy check paper" style="background:linear-gradient(180deg,#e58d9f 0 30%,#f3bfca 30% 65%,#eea9b7 65%)"></div><div class="swatch-label">Linen Burgundy (cot)</div></div>
  <div class="abs swatch" style="left:268px;top:1481px"><div class="swatch-thumb" role="img" aria-label="Linen purple check paper" style="background:linear-gradient(180deg,#9297c9 0 30%,#babde0 30% 65%,#a9acd7 65%)"></div><div class="swatch-label">Linen Purple (cot)</div></div>
  <div class="abs swatch" style="left:345px;top:1481px"><div class="swatch-thumb" role="img" aria-label="Linen gold check paper" style="background:linear-gradient(180deg,#dcc88f 0 30%,#eee2b8 30% 65%,#e7d7a6 65%)"></div><div class="swatch-label">Linen Gold (cot)</div></div>

  <div class="abs swatch" style="left:35px;top:1657px"><div class="swatch-thumb" role="img" aria-label="American flag themed check paper" style="background:linear-gradient(180deg,#d4505f 0 28%,#c7d6f2 28% 65%,#b5c6ec 65%)"></div><div class="swatch-label">American Flag (cot)</div></div>
  <div class="abs swatch" style="left:113px;top:1657px"><div class="swatch-thumb" role="img" aria-label="Blue-green gradient check paper" style="background:linear-gradient(180deg,#7f9dc7 0 28%,#c9cff2 28% 65%,#b6bdea 65%)"></div><div class="swatch-label">Blue-Green (cot)</div></div>
  <div class="abs swatch" style="left:190px;top:1657px"><div class="swatch-thumb" role="img" aria-label="Blue-red gradient check paper" style="background:linear-gradient(180deg,#9c6a9e 0 28%,#c6c9ec 28% 65%,#b4b8e3 65%)"></div><div class="swatch-label">Blue-Red (cot)</div></div>

  <a class="abs next-btn" href="#">NEXT →</a>
</section>

<section class="abs preview-panel">
  <div class="abs check-face" role="img" aria-label="Blue marble check face background">
    <span class="abs check-notice">THE FACE OF THIS DOCUMENT HAS A COLORED BACKGROUND ON WHITE PAPER</span>
    <span class="abs check-side">Security features included. Details on back.</span>
  </div>
  <div class="abs perforation" style="top:304px"></div>
  <div class="abs stub" style="top:311px"></div>
  <div class="abs perforation" style="top:559px"></div>
  <div class="abs stub" style="top:565px"></div>
  <div class="abs preview-fade"></div>
</section>

<section class="abs desc-tabs">
  <div class="abs desc-tab active" style="left:0;width:185px">OVERVIEW</div>
  <div class="abs desc-tab" style="left:185px;width:183px">ITEM SPECIFICATIONS</div>
  <div class="abs desc-tab" style="left:368px;width:183px">SHIPPING</div>
  <div class="abs desc-tab" style="left:551px;width:183px">PRODUCT REVIEWS</div>
</section>
<div class="abs desc-body">computer-checks-description.php</div>

<footer class="abs site-footer">
  <div class="abs foot-head" style="left:62px;top:51px">STAY IN TOUCH</div>
  <span class="abs social" style="left:62px;top:82px;background:#3b5998"></span>
  <span class="abs social" style="left:98px;top:82px;background:#3fa0e0"></span>
  <span class="abs social" style="left:134px;top:82px;background:#444"></span>
  <span class="abs social" style="left:170px;top:82px;background:#f08a2c;border-radius:50%"></span>
  <div class="abs foot-head" style="left:62px;top:145px">GET OUR NEWSLETTER</div>
  <div class="abs newsletter-badge">Get our Newsletter</div>

  <div class="abs foot-head" style="left:613px;top:51px">ORDER INFO</div>
  <ul class="abs foot-links" style="left:613px;top:78px"><li>Order History</li><li>Track Order &amp; Order Status</li><li>Reorder</li><li>Rush Order</li></ul>
  <div class="abs foot-head" style="left:796px;top:51px">SUPPORT</div>
  <ul class="abs foot-links" style="left:796px;top:78px"><li>Contact Us</li><li>Shipping &amp; Turnaround</li><li>Help &amp; FAQs</li></ul>
  <div class="abs foot-head" style="left:980px;top:51px">INFORMATION</div>
  <ul class="abs foot-links" style="left:980px;top:78px"><li>About Us</li><li>Privacy &amp; Security</li><li>Refunds &amp; Returns</li><li>Terms &amp; Conditions</li></ul>
</footer>

<div class="abs bottom-bar">
  <span class="abs safe-badge"></span>
  <div class="abs copyright">Copyright © 2017 ShopLedgerForms.net. | Sitemap</div>
  <span class="abs pay-mark" style="left:914px;width:20px;background:#ccc"></span>
  <span class="abs pay-mark" style="left:937px;width:18px;background:#e8a33a"></span>
  <span class="abs pay-mark" style="left:962px;width:18px;background:#8fb0d8"></span>
  <span class="abs pay-mark" style="left:991px;width:14px;background:#2f6fb8"></span>
  <span class="abs pay-mark" style="left:1010px;width:44px;background:#c9d6ea"></span>
  <span class="abs pay-mark" style="left:1058px;width:74px;background:#dfe3ea"></span>
</div>

</body>
</html>
```